Investment fund letterhead + bus.card design

We are an investment fund focused on investments in the energy sector.
Pls. use design of existing logo in the attachment.
You are free to change the colors of the logo.
However, some associations should exist on the website as well.
webpage: www.brightelmholdings.fund.
This is a contest for a letterhead and business card. Therefore, pls. present letterhead and business card at once. The winner will be selected by January 11, 12pm.

Good luck! Good luck! Good luck! Good luck! Good luck! Good luck! Good luck! Good luck! Good luck! Good luck! Good luck! Good luck! Good luck! Good luck! Good luck! Good luck! Good luck! Good luck! Good luck! Good luck! Good luck! Good luck! Good luck! Good luck! Good luck! Good luck! Good luck! Good luck! Good luck! Good luck! Good luck! Good luck! Good luck! Good luck! Good luck! Good luck! Good luck! Good luck! Good luck! Good luck! Good luck! Good luck! Good luck! Good luck! Good luck! Good luck! Good luck! Good luck! Good luck! Good luck! Good luck! Good luck! Good luck! Good luck! Good luck! Good luck! Good luck! Good luck! Good luck! Good luck! Good luck! Good luck! Good luck! Good luck! Good luck! Good luck! Good luck! Good luck! Good luck! Good luck! Good luck! Good luck! Good luck! Good luck! Good luck! Good luck! Good luck! Good luck! Good luck! Good luck! Good luck! Good luck! Good luck! Good luck! Good luck! Good luck! Good luck! Good luck! Good luck! Good luck! Good luck! Good luck! Good luck! Good luck! Good luck! Good luck! Good luck! Good luck! Good luck! Good luck! Good luck! Good luck! Good luck! Good luck! Good luck! Good luck! Good luck! Good luck! Good luck! Good luck! Good luck! Good luck! Good luck! Good luck! Good luck! Good luck! Good luck! Good luck! Good luck! Good luck! Good luck! Good luck! Good luck! Good luck! Good luck! Good luck! Good luck! Good luck! Good luck! Good luck! Good luck! Good luck! Good luck! Good luck! Good luck! Good luck! Good luck! Good luck! Good luck! Good luck! Good luck! Good luck! Good luck! Good luck! Good luck! Good luck! Good luck! Good luck! Good luck! Good luck! Good luck! Good luck! Good luck! Good luck! Good luck! Good luck! Good luck! Good luck! Good luck! Good luck! Good luck! Good luck! Good luck! Good luck! Good luck! Good luck! Good luck! Good luck! Good luck! Good luck! Good luck! Good luck! Good luck! Good luck! Good luck! Good luck! Good luck! Good luck! Good luck! Good luck! Good luck! Good luck! Good luck! Good luck! Good luck! Good luck! Good luck! Good luck! Good luck! Good luck! Good luck! Good luck! Good luck! Good luck! Good luck! Good luck! Good luck! Good luck! Good luck! Good luck! Good luck! Good luck! Good luck! Good luck! Good luck! Good luck! Good luck! Good luck! Good luck! Good luck! Good luck! Good luck! Good luck! Good luck! Good luck! Good luck! Good luck! Good luck! Good luck! Good luck! Good luck! Good luck! Good luck! Good luck! Good luck! Good luck! Good luck! Good luck! Good luck! Good luck! Good luck! Good luck! Good luck! Good luck! Good luck! Good luck! Good luck! Good luck! Good luck! Good luck! Good luck! Good luck! Good luck!

Target Market(s)

Energy companies, Financial institutions

Industry/Entity Type

Investment Banking

Contact Information for Business Card

Title, Name, contacts

Font styles to use
Serif

Colors

Designer to choose colors to be used in the design.

Requirements
Must have
• Logo
Nice to have
• Some modern design hints/design elements.

```html
<!DOCTYPE html>
<html lang="en">
<head>
<meta charset="utf-8">
<title>Bright Elm — Business Card</title>
<link href="https://fonts.googleapis.com/css2?family=Arimo:wght@400;700&display=swap" rel="stylesheet">
<style>
  :root {
    --navy: #0b2a4f;
    --grey: #8a8a8a;
    --text-grey: #6b6b6b;
    --rule: #d2d2d2;
    --paper: #f7f7f7;
    --backdrop: #dcdfe3;
    --white: #ffffff;
  }
  * { margin: 0; padding: 0; box-sizing: border-box; }
  html, body {
    width: 1200px; height: 786px; overflow: hidden;
    background: var(--backdrop);
    font-family: "Arimo", Arial, sans-serif;
  }
  .stage {
    width: 1200px; height: 786px;
    display: flex; align-items: center; justify-content: center; gap: 60px;
  }
  .card {
    width: 520px; height: 290px;
    position: relative;
    box-shadow: 0 10px 30px rgba(0,0,0,0.18);
  }
  .brand-square { display: block; background: var(--grey); flex: none; }
  .brand-name {
    font-weight: 700; text-transform: uppercase; line-height: 1; white-space: nowrap;
  }

  /* Front */
  .card-front { background: var(--paper); color: var(--text-grey); }
  .card-front .brand-mark {
    position: absolute; right: 36px; top: 96px;
    display: flex; align-items: center; gap: 12px;
  }
  .card-front .brand-square { width: 26px; height: 26px; }
  .card-front .brand-name { font-size: 26px; letter-spacing: 3px; color: var(--navy); }
  .person { position: absolute; left: 34px; top: 102px; }
  .person-name {
    font-weight: 700; font-size: 13px; color: var(--navy);
    text-transform: uppercase; letter-spacing: 0.3px;
  }
  .person-title { font-size: 11px; margin-top: 3px; }
  .contacts {
    position: absolute; left: 34px; bottom: 34px;
    display: flex; font-size: 11px; line-height: 1.5;
  }
  .contact-group { padding-right: 18px; }
  .contact-group + .contact-group {
    padding-left: 18px; border-left: 1px solid var(--rule);
  }

  /* Back */
  .card-back {
    background: var(--navy);
    display: flex; align-items: center; justify-content: center; gap: 14px;
  }
  .card-back .brand-square { width: 28px; height: 28px; }
  .card-back .brand-name { color: var(--white); font-size: 24px; letter-spacing: 6px; }
</style>
</head>
<body>
  <main class="stage">
    <section class="card card-front" aria-label="Business card front">
      <div class="person">
        <p class="person-name">Pavel Sorokin</p>
        <p class="person-title">General Manager</p>
      </div>
      <div class="brand-mark">
        <span class="brand-square" aria-hidden="true"></span>
        <span class="brand-name">Bright Elm</span>
      </div>
      <div class="contacts">
        <div class="contact-group">
          <p>+7 000 555 0142</p>
          <p>+7 000 555 0142</p>
        </div>
        <div class="contact-group">
          <p>invest@brightelm.info</p>
          <p>www.brightelmholdings.fund</p>
        </div>
        <div class="contact-group">
          <p>Kazan</p>
          <p>Energetikov str, 4-11</p>
        </div>
      </div>
    </section>

    <section class="card card-back" aria-label="Business card back">
      <span class="brand-square" aria-hidden="true"></span>
      <span class="brand-name">Bright Elm</span>
    </section>
  </main>
</body>
</html>
```